Business Card for Innovative Cannabis Consultation Service

Need attached logo refined and used in business card layout. This is for an in-home consultation and demonstration service on cannabis awareness and use of apparatus for cannabis consumption.
Updates

Logo needs to be refined, I would like to see more definition in the leaf - maybe just a little zigzig at top of leaves.  I also would like the shape of person to pop out more, to be more defined using shadows or a different color.

On the backside, I want the Molecular structure (from circular logo attached) on back, and I'd like it to say "Dare to be Aware" 

The card should convey professionalism, yet a bit of fun

I just added a new file for the molecular structure.  The design can be modified slightly.  The back should read:  "Dare to be Aware - Cannabis Awareness"  Probably two lines.

Just added a couple files in .ai format.  Hope that helps. . .

NOTE:  I apologize for the confusion regarding the "round logo".  The purpose of the round logo was to show preferred color scheme.  Please use leaf and molecular structure as separate items for business card layout.  The "leaf w/person & heart" is the logo for Plumvesta, LLC. 

Reason: I'm extending deadline due to last minute trip out of town. Thank you everyone for your submissions!

Industry/Entity Type

Business

Requirements
Must have
• Use same color scheme as attached logos. "Aware" should stand out, i.e. Plumvesta, LLC.

```html
<!DOCTYPE html>
<html lang="en">
<head>
<meta charset="utf-8">
<title>Plumvesta Business Cards</title>
<link rel="stylesheet" href="https://fonts.googleapis.com/css2?family=Bebas+Neue&family=Raleway:wght@400;500&family=Open+Sans:wght@400&display=swap">
<style>
  :root {
    --paper: #ffffff;
    --ink: #2b2b2b;
    --leaf-green: #4f7d34;
    --deep-green: #3f6a2a;
    --tan: #c3a576;
    --rule: #555555;
  }
  * { margin: 0; padding: 0; box-sizing: border-box; }
  html, body { width: 1200px; height: 1006px; overflow: hidden; background: var(--paper); }
  .sheet { position: relative; width: 1200px; height: 1006px; color: var(--ink); font-family: "Raleway", sans-serif; }
  .abs { position: absolute; }
  .sheet-label { font-family: "Open Sans", sans-serif; font-size: 16px; top: 26px; }
  .edge-line { left: 2px; top: 48px; width: 1px; height: 950px; background: #cfcfcf; }
  .cut-line { left: 911px; width: 0; border-left: 2px dashed var(--rule); }
  .name { font-family: "Bebas Neue", sans-serif; font-size: 40px; letter-spacing: 1px; line-height: 1; color: var(--ink); }
  .mark-seal { border-radius: 50%; background: var(--tan); display: flex; align-items: center; justify-content: center; }
  .mark-seal span { font-family: "Bebas Neue", sans-serif; color: var(--deep-green); letter-spacing: 1px; }
  .mark-dot { border-radius: 50%; background: var(--leaf-green); }
  .contact { font-size: 19px; line-height: 22px; text-align: right; }
  .contact-line { display: flex; align-items: center; justify-content: flex-end; gap: 10px; }
  .contact-line svg { width: 14px; height: 14px; flex: none; }
  .address { font-size: 18px; white-space: nowrap; }
  .lockup { writing-mode: vertical-rl; line-height: 1; }
  .lockup-name { font-family: "Bebas Neue", sans-serif; font-size: 32px; letter-spacing: 2px; color: var(--ink); }
  .lockup-desc { font-family: "Raleway", sans-serif; font-size: 24px; color: var(--ink); margin-top: 2px; }
  .vertical { writing-mode: vertical-lr; }
  .v-contact { font-size: 19px; line-height: 21px; }
  .v-contact .contact-line { justify-content: flex-start; gap: 8px; }
</style>
</head>
<body>
<svg width="0" height="0" style="position:absolute">
  <defs>
    <symbol id="icon-phone" viewBox="0 0 14 14"><rect x="3.5" y="1" width="7" height="12" rx="1.2" fill="none" stroke="#555" stroke-width="1.3"/><rect x="5" y="3" width="4" height="4" fill="#555"/></symbol>
    <symbol id="icon-mail" viewBox="0 0 14 14"><rect x="1" y="3" width="12" height="8" fill="none" stroke="#555" stroke-width="1.2"/><path d="M1 3 L7 8 L13 3 M1 11 L5.5 7 M13 11 L8.5 7" fill="none" stroke="#555" stroke-width="1.1"/></symbol>
    <symbol id="icon-web" viewBox="0 0 14 14"><circle cx="7" cy="7" r="5.8" fill="none" stroke="#555" stroke-width="1.2"/><ellipse cx="7" cy="7" rx="2.6" ry="5.8" fill="none" stroke="#555" stroke-width="1"/><path d="M1.2 7 H12.8" stroke="#555" stroke-width="1"/></symbol>
  </defs>
</svg>

<main class="sheet">
  <div class="abs sheet-label" style="left:0">Business Card 1</div>
  <div class="abs sheet-label" style="left:656px">Business Card 3</div>
  <div class="abs edge-line"></div>

  <!-- Card 1, front -->
  <section class="card card-one-front">
    <div class="abs mark-seal" style="left:18px;top:78px;width:174px;height:174px"><span style="font-size:34px">Plumvesta</span></div>
    <div class="abs name" style="right:772px;top:80px">Jane Doe</div>
    <svg class="abs" style="left:296px;top:118px" width="138" height="18" viewBox="0 0 138 18"><path d="M2 14 C30 4 70 4 100 8 C115 10 125 8 136 2" fill="none" stroke="var(--leaf-green)" stroke-width="3.4" stroke-linecap="round"/></svg>
    <div class="abs contact" style="right:770px;top:168px">
      <div class="contact-line">+ 1 800 555 1234 <svg><use href="#icon-phone"/></svg></div>
      <div class="contact-line">hello@email.com <svg><use href="#icon-mail"/></svg></div>
      <div class="contact-line">www.plumvesta.com <svg><use href="#icon-web"/></svg></div>
    </div>
    <div class="abs address" style="right:770px;top:282px">1234 Adress Here St. City, State, 12345</div>
  </section>

  <!-- Card 1, back -->
  <section class="card card-one-back">
    <div class="abs mark-dot" style="left:30px;top:530px;width:200px;height:200px"></div>
    <div class="abs lockup" style="left:118px;top:780px">
      <span class="lockup-name">Plumvesta</span>
      <span class="lockup-desc">consultants</span>
    </div>
  </section>

  <!-- Card 3 -->
  <div class="abs cut-line" style="top:0;height:45px"></div>
  <div class="abs cut-line" style="top:525px;height:48px"></div>
  <section class="card card-three">
    <div class="abs name vertical" style="left:672px;top:87px;font-size:38px">Jane Doe</div>
    <svg class="abs" style="left:708px;top:88px" width="16" height="130" viewBox="0 0 16 130"><path d="M4 2 C13 30 13 70 9 100 C8 112 10 120 14 128" fill="none" stroke="var(--leaf-green)" stroke-width="3.4" stroke-linecap="round"/></svg>
    <div class="abs vertical v-contact" style="left:764px;top:80px">
      <div class="contact-line"><svg><use href="#icon-phone"/></svg>+ 1 800 555 1234</div>
      <div class="contact-line"><svg><use href="#icon-mail"/></svg>hello@email.com</div>
      <div class="contact-line"><svg><use href="#icon-web"/></svg>www.plumvesta.com</div>
    </div>
    <div class="abs mark-seal" style="left:670px;top:322px;width:174px;height:174px"><span style="font-size:30px">Plumvesta</span></div>
    <div class="abs address vertical" style="left:874px;top:84px">1234 Adress Here St. City, State, 12345</div>
    <div class="abs mark-dot" style="left:942px;top:86px;width:200px;height:200px"></div>
    <div class="abs lockup" style="left:1016px;top:330px">
      <span class="lockup-name">Plumvesta</span>
      <span class="lockup-desc">consultants</span>
    </div>
  </section>
</main>
</body>
</html>
```